Adventurous female pilot

I am looking for a personal business card, for a very well qualified female pilot, with a lot of aviation experience.

Currently an airline pilot, have worked as a bush pilot in Africa, looking to get into corporate aviation, or private jet owners.
Want a classy looking card for networking...

Could be interested in a retro\vintage look also?!

An idea,, is an african sunset background, with my wings\logo on it
Updates

I just want to say thank you to all of your for your amazing designs!

I have been very busy flying this past week , so not had a chance to be on the computer much.
But I provide some feedback, and conclusions very soon!
Thank you again.

Marla

Reason: Still waiting on a couple of revisions to be 100% about my choice!

Target Market(s)

corporate aviation, private jet owners, casino's,
General audience.
networking

Industry/Entity Type

Airline

Requirements
Nice to have
• Classy, edgy, sexy, but also feminine

```html
<!DOCTYPE html>
<html lang="en">
<head>
<meta charset="UTF-8">
<title>Marla Halden Aviation – Business Card</title>
<link rel="stylesheet" href="https://fonts.googleapis.com/css2?family=Josefin+Sans:wght@400&family=Varela+Round&display=swap">
<style>
  :root {
    --sky-top: #9a6c6e;
    --sky-mid: #c98f74;
    --sun-glow: #f6c274;
    --horizon: #d9a57a;
    --grass: #6b6a69;
    --ink: #1d1d1f;
    --ink-soft: #6d6a68;
    --white: #ffffff;
  }
  html, body {
    margin: 0;
    padding: 0;
    width: 1200px;
    height: 661px;
    overflow: hidden;
    background: var(--white);
  }
  .card {
    position: relative;
    width: 1200px;
    height: 661px;
    overflow: hidden;
  }
  .savanna-scene {
    position: absolute;
    inset: 0;
    background:
      radial-gradient(ellipse 230px 220px at 575px 175px, var(--sun-glow) 0%, rgba(246,194,116,0.75) 45%, rgba(246,194,116,0) 100%),
      linear-gradient(to bottom, var(--sky-top) 0%, var(--sky-mid) 38%, var(--horizon) 62%, #b89078 72%, var(--grass) 82%, var(--grass) 100%);
  }
  .frame-top {
    position: absolute;
    left: 0;
    top: 4px;
    width: 1142px;
    height: 3px;
    background: var(--white);
  }
  .frame-right {
    position: absolute;
    left: 1139px;
    top: 4px;
    width: 3px;
    height: 657px;
    background: var(--white);
  }
  .brand {
    position: absolute;
    left: 0;
    width: 1162px;
    top: 300px;
    text-align: center;
    font-family: "Josefin Sans", sans-serif;
    font-weight: 400;
    color: var(--ink);
  }
  .brand-name {
    display: block;
    font-size: 33px;
    letter-spacing: 0.5px;
    line-height: 40px;
  }
  .brand-line {
    display: block;
    font-size: 21px;
    letter-spacing: 1px;
    line-height: 28px;
  }
  .contact {
    position: absolute;
    font-family: "Varela Round", sans-serif;
    font-size: 23px;
    color: var(--white);
    letter-spacing: 1.2px;
    white-space: nowrap;
  }
  .contact-us { left: 75px; top: 510px; }
  .contact-taipei { left: 614px; top: 510px; }
  .contact-email { left: 75px; top: 563px; letter-spacing: 0.6px; }
</style>
</head>
<body>
  <main class="card">
    <div class="savanna-scene" role="img" aria-label="African savanna at sunset with a glowing sun, acacia trees and silhouetted giraffes, elephants and a zebra"></div>
    <div class="frame-top"></div>
    <div class="frame-right"></div>

    <div class="brand">
      <span class="brand-name">MARLA HALDEN</span>
      <span class="brand-line">AVIATION</span>
    </div>

    <p class="contact contact-us" style="margin:0">Cell&nbsp; US:&nbsp; +1.702.555.0143</p>
    <p class="contact contact-taipei" style="margin:0">Cell&nbsp; Taipei:&nbsp; +886.900.555.126</p>
    <p class="contact contact-email" style="margin:0">Email:&nbsp; marla.halden@skymail.net</p>
  </main>
</body>
</html>
```